Vorn Solutions: searching for a flyer to trow in letterboxes for properties we are interested in

Hello ,

Introduction:
We are a company based in Luxembourg called "Vorn Solutions". We are specialized in buying properties on which we develop and build constructions before selling them.

Informations for the flyer:
We need a flyer to trow into the letter boxes of property owners letting them know that we are interested in buying their property, if they are interested they can give us a call.

The text for the flyer/letter is in the attachment called >>2020-03-11_VS_Text for flyer,letter there might be slight changes<<.

We need to look competent, professional and financially stable.

The flyer needs to be short and not over welling with information otherwise it will land in the trash.

We have decided that we don't want real pictures on the flyer, but shapes of any kind, blue prints, drawings are fine.

Format should be in DIN A4. We plan to print the flyer on both sides in two different languages, in other words the design will be the same on both sides only the text will be in a different language.

I also added our current logo and here is the design of the website that is under construction at the moment http://www.vornsolutions.example/. The logo's color can be changed into a different blue or uni color (all white or all black).
Updates

Hi, First time user the howl thing started faster as expected. Furthermore, I need to catch my boss to discust the project with him and he is on a lot of meetings. Please give us a little bit more time. Thanks

Target Market(s)

Property owners

Requirements
Must have
• email, phone number, tax number (RCS), Tax number , matriculation and address.
see word file in attachment for information
Nice to have
• Our company logo, in one form or an other, you can be creative, the logo is in the attachment.
Should not have
• Real pictures

```html
<!DOCTYPE html>
<html lang="fr">
<head>
<meta charset="utf-8">
<title>Vorn Solutions – Lettre propriétaires</title>
<link rel="stylesheet" href="https://fonts.googleapis.com/css2?family=Arimo:wght@400&family=Oswald:wght@600&display=swap">
<style>
  :root{
    --backdrop:#303030;
    --paper:#ffffff;
    --brand-blue:#0a5e8c;
    --brand-blue-dark:#064e78;
    --shard-black:#141414;
    --ink:#1a1a1a;
    --skyline-light:#f2f2f2;
    --skyline-grey:#c9c9c9;
  }
  *{margin:0;padding:0;box-sizing:border-box}
  html,body{width:1200px;height:1200px;overflow:hidden;background:var(--backdrop)}
  .board{position:relative;width:1200px;height:1200px}
  .letter{position:absolute;top:210px;width:552px;height:776px;background:var(--paper);overflow:hidden;
    font-family:"Arimo",Arial,sans-serif;color:var(--ink);font-size:12px;line-height:15px}
  .letter--fr{left:32px}
  .letter--lb{left:624px;top:211px}
  .letter__shapes{position:absolute;inset:0;width:552px;height:776px}
  .brand-mark{position:absolute;left:76px;top:152px;width:36px;height:50px;background:var(--brand-blue)}
  .brand-name{position:absolute;left:43px;top:210px;font-family:"Oswald",Arial Narrow,sans-serif;font-weight:600;
    font-size:18px;letter-spacing:.2px;color:var(--brand-blue);line-height:22px}
  .brand-legal{position:absolute;left:43px;top:233px;font-size:12px}
  .contact{position:absolute;left:43px;font-size:12px}
  .contact__icon{position:absolute;left:-17px;top:2px;width:11px;height:11px}
  .contact--address{top:256px}
  .contact--email{top:293px}
  .contact--phone{top:314px}
  .date-line{position:absolute;left:396px;top:344px;font-size:12px}
  .body-text{position:absolute;left:43px;width:470px;font-size:12px}
</style>
</head>
<body>
<div class="board">

  <article class="letter letter--fr">
    <svg class="letter__shapes" viewBox="0 0 690 969" preserveAspectRatio="none" aria-hidden="true">
      <defs>
        <linearGradient id="skyFr" x1="0" y1="0" x2="0" y2="1">
          <stop offset="0" stop-color="var(--paper)"/>
          <stop offset="1" stop-color="var(--skyline-grey)"/>
        </linearGradient>
        <linearGradient id="shardFr" x1="0" y1="0" x2="1" y2="1">
          <stop offset="0" stop-color="#555"/>
          <stop offset="1" stop-color="var(--shard-black)"/>
        </linearGradient>
      </defs>
      <rect x="0" y="740" width="690" height="229" fill="url(#skyFr)" role="img" aria-label="Silhouette grise de chantier urbain avec grues et immeubles"/>
      <polygon points="0,0 690,0 690,158 428,93 370,133 185,53 0,198" fill="var(--brand-blue)"/>
      <polygon points="80,3 428,93 370,133" fill="url(#shardFr)"/>
      <polygon points="0,846 230,898 500,969 0,969" fill="var(--brand-blue-dark)"/>
      <polygon points="200,898 245,870 510,969 470,969" fill="url(#shardFr)"/>
    </svg>

    <div class="brand-mark"></div>
    <div class="brand-name">VORN SOLUTIONS</div>
    <div class="brand-legal">Vorn Solutions sàrl</div>

    <div class="contact contact--address">
      <svg class="contact__icon" viewBox="0 0 12 12"><path d="M6 0.5a4 4 0 0 1 4 4c0 3-4 7-4 7s-4-4-4-7a4 4 0 0 1 4-4z" fill="var(--brand-blue)"/><circle cx="6" cy="4.5" r="1.5" fill="#fff"/></svg>
      17 rue des Ateliers, L-4321<br>Esch-Neuville
    </div>
    <div class="contact contact--email">
      <svg class="contact__icon" viewBox="0 0 12 12"><rect x="0.5" y="2.5" width="11" height="7" fill="var(--brand-blue)"/><path d="M0.5 2.5l5.5 4 5.5-4" stroke="#fff" fill="none"/></svg>
      info@vornsolutions.example
    </div>
    <div class="contact contact--phone">
      <svg class="contact__icon" viewBox="0 0 12 12"><circle cx="6" cy="6" r="5.2" fill="none" stroke="var(--brand-blue)"/><path d="M4 3.5l1 1-0.6 0.9c.4.9 1.1 1.6 2 2l.9-.6 1 1-.8.9C5.6 8.5 3.6 6.5 3.4 4.3z" fill="var(--brand-blue)"/></svg>
      691 555 014
    </div>

    <div class="date-line">Date :&nbsp;&nbsp; /&nbsp;&nbsp;&nbsp; / 20</div>

    <p class="body-text" style="top:390px">Madame/Monsieur,</p>
    <p class="body-text" style="top:420px">Ce courrier vous a été adressé, car votre propriété a attiré notre attention. Nous souhaiterions discuter avec vous de son éventuel rachat par notre société.</p>
    <p class="body-text" style="top:466px">En cas d’accord, nous vous assurons une décision rapide, un paiement garanti, et zéro frais d’intermédiaire.</p>
    <p class="body-text" style="top:511px">En attendant de vos nouvelles, nous restons à votre entière disposition pour tout renseignement.</p>
    <p class="body-text" style="top:557px">Salutations distinguées,</p>
    <p class="body-text" style="top:587px">L’équipe de Vorn Solutions</p>
  </article>

  <article class="letter letter--lb" lang="lb">
    <svg class="letter__shapes" viewBox="0 0 690 969" preserveAspectRatio="none" aria-hidden="true">
      <defs>
        <linearGradient id="skyLb" x1="0" y1="0" x2="0" y2="1">
          <stop offset="0" stop-color="var(--paper)"/>
          <stop offset="1" stop-color="var(--skyline-grey)"/>
        </linearGradient>
        <linearGradient id="shardLb" x1="0" y1="0" x2="1" y2="1">
          <stop offset="0" stop-color="#555"/>
          <stop offset="1" stop-color="var(--shard-black)"/>
        </linearGradient>
      </defs>
      <rect x="0" y="740" width="690" height="229" fill="url(#skyLb)" role="img" aria-label="Silhouette grise de chantier urbain avec grues et immeubles"/>
      <polygon points="0,0 690,0 690,158 428,93 370,133 185,53 0,198" fill="var(--brand-blue)"/>
      <polygon points="80,3 428,93 370,133" fill="url(#shardLb)"/>
      <polygon points="0,846 230,898 500,969 0,969" fill="var(--brand-blue-dark)"/>
      <polygon points="200,898 245,870 510,969 470,969" fill="url(#shardLb)"/>
    </svg>

    <div class="brand-mark"></div>
    <div class="brand-name">VORN SOLUTIONS</div>
    <div class="brand-legal">Vorn Solutions sàrl</div>

    <div class="contact contact--address">
      <svg class="contact__icon" viewBox="0 0 12 12"><path d="M6 0.5a4 4 0 0 1 4 4c0 3-4 7-4 7s-4-4-4-7a4 4 0 0 1 4-4z" fill="var(--brand-blue)"/><circle cx="6" cy="4.5" r="1.5" fill="#fff"/></svg>
      17 rue des Ateliers, L-4321<br>Esch-Neuville
    </div>
    <div class="contact contact--email">
      <svg class="contact__icon" viewBox="0 0 12 12"><rect x="0.5" y="2.5" width="11" height="7" fill="var(--brand-blue)"/><path d="M0.5 2.5l5.5 4 5.5-4" stroke="#fff" fill="none"/></svg>
      info@vornsolutions.example
    </div>
    <div class="contact contact--phone">
      <svg class="contact__icon" viewBox="0 0 12 12"><circle cx="6" cy="6" r="5.2" fill="none" stroke="var(--brand-blue)"/><path d="M4 3.5l1 1-0.6 0.9c.4.9 1.1 1.6 2 2l.9-.6 1 1-.8.9C5.6 8.5 3.6 6.5 3.4 4.3z" fill="var(--brand-blue)"/></svg>
      691 555 014
    </div>

    <div class="date-line">Date :&nbsp;&nbsp; /&nbsp;&nbsp;&nbsp; / 20</div>

    <p class="body-text" style="top:390px">Madame / Monsieur,</p>
    <p class="body-text" style="top:420px;width:490px">Dir kritt dëst Schreiwes well Är Proprietéit eis Opmierksamkeet zeréckbehalen huet. Mir géinge gär mat Iech iwwert d’Méiglechkeet, datt eise Betrib se opkeeft, diskutéieren.</p>
    <p class="body-text" style="top:466px">Mir versécheren Iech e séieren Entscheedungsprozess, garantéierend’ Bezuelung a verrechne keng Drëttkäschten.</p>
    <p class="body-text" style="top:511px">Mir géinge neis freeën, vun Iech ze héieren, a sti ganz zu Ärer Verfügung fir zousätzlech Informatiounen.</p>
    <p class="body-text" style="top:557px">Mat beschte Gréiss,</p>
    <p class="body-text" style="top:587px">D’Equipe vun Vorn Solutions</p>
  </article>

</div>
</body>
</html>
```